Lumen Systems New Website - IT Infrastructure | Smart Cabinet | Micro Data Center

We're an IT SI providing Server Room Design & Build | All-in-One Rack & Smart Cabinet | Structured Cabling | IT Relocation | Maintenance. Old website can be found at www.lumensys-demo.com.hk. We'd like a brand new wix website which is modern, minimalist, interactive with some animation. Website content will be mostly static and include our service, our project, news and events, about us, contacts, blogs, partners and brands, etc.

reference sites:
We'd like to see more designs referring to below

https://www.pixelbidhub.example/design/40517736
https://www.pixelbidhub.example/design/40592214
https://velbrix.example/

Animation (scrolling effect) referring to
https://velbrix.example/intelligence/smart-office-room/
Updates

we'd like below style.

Designs look the same

Target Market(s)

Commercials in HK

Industry/Entity Type

IT, Technology, Data Center

Coding

Coded - Design and coding required

Font styles to use
Sans Serif

Requirements
Must have
• CMS, Some Interactive Elements/ Graphics

```html
<!DOCTYPE html>
<html lang="en">
<head>
<meta charset="utf-8">
<title>Lumen Systems — IT Infrastructure</title>
<link href="https://fonts.googleapis.com/css2?family=Fira+Sans:wght@400;500;600;700&family=Open+Sans:wght@400;600;700&display=swap" rel="stylesheet">
<style>
:root{
  --orange:#ff7a00;
  --navy:#0b1e45;
  --navy-2:#13284f;
  --ink:#2a3f66;
  --text:#6b6f78;
  --light:#f2f3f5;
  --white:#ffffff;
  --field:#4b5877;
}
*{box-sizing:border-box;margin:0;padding:0}
html,body{width:1200px;height:4177px;overflow:hidden}
body{position:relative;font-family:"Open Sans",sans-serif;color:var(--text);background:var(--white)}
.abs{position:absolute}
h1,h2,h3,h4,.brand{font-family:"Fira Sans",sans-serif}
.label{font-family:"Fira Sans",sans-serif;font-weight:600;color:var(--orange);font-size:16px}
.btn{position:absolute;display:flex;align-items:center;justify-content:center;gap:10px;background:var(--orange);color:#fff;font-family:"Fira Sans",sans-serif;font-weight:600;font-size:16px}
.photo{position:absolute}

/* header */
.topbar{left:385px;top:0;width:815px;height:33px;background:var(--ink);clip-path:polygon(0 0,100% 0,100% 100%,25px 100%);display:flex;align-items:center;font-size:11px;font-weight:700;color:#fff}
.topbar .item{display:flex;align-items:center;gap:8px;height:100%}
.topbar .phone{position:absolute;left:60px}
.topbar .appt{position:absolute;left:210px;width:232px;background:var(--orange);justify-content:center}
.topbar .addr{position:absolute;left:474px}
.brand{font-weight:600;color:var(--orange);font-size:26px;display:flex;align-items:center;gap:10px}
.brand .mark{width:30px;height:30px;border:3px solid var(--orange)}
.nav{top:58px;left:0;width:1200px;font-size:12px;color:#333}
.nav span{position:absolute;top:0;transform:translateX(-50%)}
.nav .home{font-weight:700}
.contact-btn{left:932px;top:54px;width:117px;height:29px;border:1.5px solid #333;font-size:11px;font-weight:700;display:flex;align-items:center;justify-content:center;color:#333;border-radius:2px}

/* hero */
.hero{left:0;top:102px;width:1200px;height:616px;background:linear-gradient(100deg,#3a2a22 0%,#24324a 35%,#1a2436 60%,#3b2d2a 100%)}
.welcome{left:517px;top:300px;width:162px;height:36px;background:#3b4b6a;color:#fff;font-size:11px;font-weight:700;display:flex;align-items:center;justify-content:center}
.hero-title{left:0;top:345px;width:1200px;text-align:center;color:#fff;font-weight:600;font-size:62px;line-height:71px}
.hero-btn{left:517px;top:519px;width:162px;height:44px;border:1.5px solid #fff;color:#fff;font-size:11px;font-weight:700;display:flex;align-items:center;justify-content:center}

/* about */
.about-h{left:640px;top:858px;color:var(--ink);font-size:48px;font-weight:600;line-height:57px}
.about-p{left:640px;top:978px;width:455px;font-size:14px;line-height:24px}

/* services */
.services{left:0;top:1359px;width:1200px;height:671px;background:var(--navy)}
.center{left:0;width:1200px;text-align:center}
.sec-title{font-size:48px;font-weight:600}
.card-box{position:absolute;width:287px;height:78px;background:#fff;border-radius:4px;text-align:center;padding-top:12px}
.card-box h4{font-size:18px;font-weight:600;color:var(--ink)}
.card-box p{font-size:12px;margin-top:6px}
.svc-icon{position:absolute;width:78px;height:78px;border-radius:50%;background:var(--orange);display:flex;align-items:center;justify-content:center;box-shadow:0 0 0 12px rgba(11,30,69,1),0 0 0 13px rgba(255,255,255,.5)}

/* mission */
.mission{left:0;top:2030px;width:1200px;height:594px;background:var(--light)}
.mission-h{left:107px;top:2117px;color:var(--ink);font-size:36px;font-weight:600;line-height:44px}
.tab{position:absolute;top:2235px;height:43px;background:#fff;font-family:"Fira Sans",sans-serif;font-size:16px;display:flex;align-items:center;padding-left:14px;color:var(--text);box-shadow:0 1px 3px rgba(0,0,0,.08)}
.tab.on{background:var(--orange);color:#fff;font-weight:600}
.mission-p{left:370px;top:2320px;width:320px;font-size:14px;line-height:24px}
.check{left:368px;font-size:14px;display:flex;align-items:center;gap:10px}

/* contact band */
.cta{left:0;top:2624px;width:1200px;height:434px;background:linear-gradient(90deg,#1f2f55 0%,#263a64 55%,#1a2a4e 100%)}
.cta-h{left:109px;top:2772px;color:#fff;font-size:46px;font-weight:600;line-height:57px}
.form-title{left:692px;top:2704px;width:394px;text-align:center;color:#fff;font-family:"Fira Sans",sans-serif;font-size:23px;font-weight:500}
.field{position:absolute;left:692px;width:394px;height:47px;background:var(--field);border-radius:4px;color:#fff;font-size:13px;font-weight:700;padding-left:52px;display:flex;align-items:center}
.submit{left:692px;top:2950px;width:394px;height:45px;border-radius:4px;font-size:16px}

/* testimonials */
.t-photo{position:absolute;width:87px;height:121px;background:linear-gradient(180deg,#d7d9dd,#8a8f98)}
.t-name{position:absolute;font-family:"Fira Sans",sans-serif;font-weight:500;color:#333;font-size:17px}
.t-city{position:absolute;font-size:12px;color:#999}
.t-card{position:absolute;width:304px;height:162px;background:#fff;box-shadow:0 2px 14px rgba(0,0,0,.1);padding:36px 18px 0 36px;font-size:14px;line-height:24px}
.t-quote{position:absolute;font-family:"Fira Sans",sans-serif;font-weight:700;font-size:64px;color:var(--orange);line-height:1}

/* footer */
.footer{left:0;top:3751px;width:1200px;height:426px;background:var(--navy)}
.f-h{color:#fff;font-family:"Fira Sans",sans-serif;font-weight:600;font-size:19px}
.f-p{color:#fff;font-size:12px;font-weight:700;line-height:24px}
.social{position:absolute;top:4030px;width:30px;height:30px;border:1px solid #3b4d76;background:#14295a}
.f-input{left:517px;top:3992px;width:223px;height:43px;background:#24386a;color:#fff;font-size:12px;font-weight:600;display:flex;align-items:center;padding-left:14px;border-radius:2px}
</style>
</head>
<body>

<!-- header -->
<div class="abs brand" style="left:133px;top:29px"><span class="mark"></span>Lumen Systems</div>
<div class="abs topbar">
  <div class="item phone"><svg width="12" height="12" viewBox="0 0 24 24" fill="none" stroke="#fff" stroke-width="2"><path d="M5 3h4l2 5-3 2a11 11 0 0 0 6 6l2-3 5 2v4a2 2 0 0 1-2 2A17 17 0 0 1 3 5a2 2 0 0 1 2-2z"/></svg>512 - 555 - 0148</div>
  <div class="item appt"><svg width="14" height="12" viewBox="0 0 24 20" fill="none" stroke="#fff" stroke-width="2"><rect x="2" y="2" width="20" height="16"/><path d="M2 3l10 8 10-8"/></svg>REQUEST AN APPOINTMENT</div>
  <div class="item addr"><svg width="11" height="13" viewBox="0 0 20 24" fill="none" stroke="#fff" stroke-width="2"><path d="M10 23s8-8 8-13a8 8 0 0 0-16 0c0 5 8 13 8 13z"/><circle cx="10" cy="10" r="3"/></svg>88 Harbour Road Wan Chai</div>
</div>
<div class="abs nav">
  <span class="home" style="left:383px">HOME</span>
  <span style="left:491px">About Us</span>
  <span style="left:611px">Services</span>
  <span style="left:723px">Our Team</span>
  <span style="left:811px">Projects</span>
</div>
<div class="abs contact-btn">CONTACT US</div>

<!-- hero -->
<div class="photo hero" role="img" aria-label="Server room corridor with glowing racks"></div>
<div class="abs welcome">WELCOME</div>
<h1 class="abs hero-title">Pioneering Tomorrow's<br>Digital Landscape</h1>
<div class="abs hero-btn">LEARN MORE</div>

<!-- about -->
<svg class="abs" style="left:86px;top:800px" width="502" height="502" viewBox="0 0 502 502">
  <polygon points="251,0 370,119 251,238 132,119" fill="#6f8196" role="img" aria-label="Engineer smiling in server room"/>
  <polygon points="132,134 251,253 132,372 13,253" fill="#2a4f86" role="img" aria-label="Rows of server racks"/>
  <polygon points="370,134 489,253 370,372 251,253" fill="#4c5763" role="img" aria-label="Technician on the phone"/>
  <polygon points="251,268 370,387 251,502 132,387" fill="#36464f" role="img" aria-label="Network cabling in rack"/>
  <circle cx="251" cy="251" r="47" fill="#fff"/>
</svg>
<div class="abs label" style="left:640px;top:830px">About Us</div>
<h2 class="abs about-h">Seamless Integration,<br>Infinite Possibilities</h2>
<p class="abs about-p">Lorem ipsum dolor sit amet, consectetur adipiscing elit, sed do eiusmod tempor incididunt ut labore et dolore magna aliqua. Ut enim ad minim veniam, quis nostrud exercitation ullamco laboris nisi ut aliquip ex ea commodo consequat. Duis aute irure dolor in reprehenderit in voluptate velit esse cillum dolore eu fugiat nulla pariatur. Excepteur sint occaecat cupidatat non proident, sunt in culpa qui officia deserunt mollit. ehenderit in voluptate velit esse cillum dolore eu fugiat nulla pariatur. Excepteur sint occaecat cup idatat non proident, sunt in culpa qui officia.</p>
<div class="btn" style="left:640px;top:1218px;width:155px;height:44px">Learn More
  <svg width="18" height="14" viewBox="0 0 18 14" fill="none" stroke="#fff" stroke-width="2"><path d="M1 7h15M10 1l6 6-6 6"/></svg></div>

<!-- services -->
<div class="abs services"></div>
<div class="abs center label" style="top:1464px">Services</div>
<h2 class="abs center sec-title" style="top:1494px;color:#fff">Our Services</h2>

<div class="photo" style="left:94px;top:1659px;width:319px;height:242px;background:linear-gradient(180deg,#2c3a4e,#121b28)" role="img" aria-label="Engineer with laptop in data centre"></div>
<div class="photo" style="left:441px;top:1659px;width:318px;height:242px;background:linear-gradient(180deg,#3e5a7c,#1b2a3e)" role="img" aria-label="Technician with laptop in server hall"></div>
<div class="photo" style="left:785px;top:1659px;width:319px;height:242px;background:linear-gradient(135deg,#5d84c7,#1f3a78)" role="img" aria-label="Close-up of blue-lit server units"></div>

<div class="svc-icon" style="left:214px;top:1617px"><svg width="32" height="32" viewBox="0 0 32 32" fill="none" stroke="#fff" stroke-width="2"><path d="M16 4l11 8-4 14H9L5 12z"/><circle cx="16" cy="16" r="4"/></svg></div>
<div class="svc-icon" style="left:559px;top:1617px"><svg width="32" height="32" viewBox="0 0 32 32" fill="none" stroke="#fff" stroke-width="2"><circle cx="16" cy="16" r="12"/><path d="M16 16l6-6M8 16h2M22 16h2M16 8v2"/></svg></div>
<div class="svc-icon" style="left:903px;top:1617px"><svg width="32" height="32" viewBox="0 0 32 32" fill="none" stroke="#fff" stroke-width="2"><path d="M6 26h20M10 26l4-8M14 18l8-10M18 12l4 4"/><circle cx="14" cy="18" r="2"/></svg></div>

<div class="card-box" style="left:109px;top:1868px"><h4>Data Centre Building</h4><p>Read More &nbsp;›</p></div>
<div class="card-box" style="left:455px;top:1868px"><h4>Structured Cabling</h4><p>Read More &nbsp;›</p></div>
<div class="card-box" style="left:798px;top:1868px"><h4>Audio-Visual</h4><p>Read More &nbsp;›</p></div>

<!-- mission -->
<div class="abs mission"></div>
<div class="photo" style="left:778px;top:2076px;width:422px;height:548px;background:linear-gradient(180deg,#eef0f3 0%,#c9ccd2 45%,#6c7584 100%);border-radius:40% 0 0 0" role="img" aria-label="Two colleagues reviewing a tablet"></div>
<h2 class="abs mission-h">Data Unleashed,<br>Connectivity Redefined</h2>
<div class="tab on" style="left:107px;width:161px">Our Mission</div>
<div class="tab" style="left:282px;width:161px">Our Vision</div>
<div class="tab" style="left:465px;width:148px">Our awards</div>
<div class="photo" style="left:107px;top:2322px;width:221px;height:229px;background:linear-gradient(180deg,#3a4a60,#141d2a);border-radius:4px" role="img" aria-label="Engineer working beside server racks"></div>
<p class="abs mission-p">Lorem ipsum dolor sit amet, consectetur eiusmod tempor incididunt ut labore et dolore im ad minim veniam, quis nostrud exercitation eiusmod tempor incididunt ut labore et dolore im ad minim veniam, quis nostrud exercitation</p>
<div class="abs check" style="top:2456px"><svg width="16" height="16" viewBox="0 0 16 16" fill="none" stroke="var(--orange)" stroke-width="1.6"><rect x="1" y="3" width="12" height="12"/><path d="M4 8l3 3 8-9"/></svg>Award winning company</div>
<div class="abs check" style="top:2490px"><svg width="16" height="16" viewBox="0 0 16 16" fill="none" stroke="var(--orange)" stroke-width="1.6"><rect x="1" y="3" width="12" height="12"/><path d="M4 8l3 3 8-9"/></svg>Award winning company</div>
<div class="abs check" style="top:2525px"><svg width="16" height="16" viewBox="0 0 16 16" fill="none" stroke="var(--orange)" stroke-width="1.6"><rect x="1" y="3" width="12" height="12"/><path d="M4 8l3 3 8-9"/></svg>Award winning company</div>

<!-- contact band -->
<div class="photo cta" role="img" aria-label="Dim blue data centre aisle"></div>
<h2 class="abs cta-h">Speed, Precision,<br>Connectivity - The<br>Trifecta of Excellence</h2>
<div class="abs form-title">Get in touch with us</div>
<div class="field" style="top:2752px">Full Name</div>
<div class="field" style="top:2818px">Email Address</div>
<div class="field" style="top:2883px">Industry</div>
<div class="btn submit">SUBMIT</div>

<!-- testimonials -->
<div class="abs center label" style="top:3146px">Testimonials</div>
<h2 class="abs center sec-title" style="top:3176px;color:var(--ink)">Clients Reviews</h2>

<div class="t-card" style="left:110px;top:3389px">Lorem ipsum dolor sit amet, consect etur adipiscing elit, sed do eiusmod tempor incididunt ut labore et dolore magna aliqua. Ut enim ad minim veni am, quis nostrud</div>
<div class="t-photo" style="left:91px;top:3284px" role="img" aria-label="Client portrait"></div>
<div class="t-name" style="left:203px;top:3304px">Adrian Sloane</div>
<div class="t-city" style="left:205px;top:3332px">Brussels</div>
<div class="t-quote" style="left:357px;top:3372px">“</div>

<div class="t-card" style="left:459px;top:3389px">Lorem ipsum dolor sit amet, consect etur adipiscing elit, sed do eiusmod tempor incididunt ut labore et dolore magna aliqua. Ut enim ad minim veni am, quis nostrud</div>
<div class="t-photo" style="left:439px;top:3284px" role="img" aria-label="Client portrait"></div>
<div class="t-name" style="left:545px;top:3304px">Tessa Turnbull</div>
<div class="t-city" style="left:547px;top:3332px">Brussels</div>
<div class="t-quote" style="left:703px;top:3372px">“</div>

<div class="t-card" style="left:808px;top:3389px">Lorem ipsum dolor sit amet, consect etur adipiscing elit, sed do eiusmod tempor incididunt ut labore et dolore magna aliqua. Ut enim ad minim veni am, quis nostrud</div>
<div class="t-photo" style="left:788px;top:3284px" role="img" aria-label="Client portrait"></div>
<div class="t-name" style="left:886px;top:3304px">Marcus Salim</div>
<div class="t-city" style="left:888px;top:3332px">Brussels</div>
<div class="t-quote" style="left:1052px;top:3372px">“</div>

<div class="btn" style="left:520px;top:3626px;width:155px;height:44px">Learn More
  <svg width="18" height="14" viewBox="0 0 18 14" fill="none" stroke="#fff" stroke-width="2"><path d="M1 7h15M10 1l6 6-6 6"/></svg></div>

<!-- footer -->
<div class="abs footer"></div>
<div class="abs brand" style="left:117px;top:3850px;font-size:28px"><span class="mark"></span>Lumen Systems</div>
<p class="abs f-p" style="left:113px;top:3932px;width:210px">Subscribe to our newsletter to recieve updates or the latest news</p>
<div class="social" style="left:115px"></div>
<div class="social" style="left:155px"></div>
<div class="social" style="left:196px"></div>
<div class="social" style="left:236px"></div>

<div class="abs f-h" style="left:517px;top:3853px">Newsletter</div>
<p class="abs f-p" style="left:517px;top:3901px;width:210px">Subscribe to our newsletter to recieve updates or the latest news</p>
<div class="abs f-input">Subscribe with us
  <svg style="position:absolute;right:14px" width="9" height="14" viewBox="0 0 9 14" fill="none" stroke="#fff" stroke-width="2"><path d="M1 1l6 6-6 6"/></svg></div>

<div class="abs f-h" style="left:859px;top:3853px">Contacts</div>
<svg class="abs" style="left:862px;top:3900px" width="32" height="36" viewBox="0 0 32 36" fill="none" stroke="var(--orange)" stroke-width="2"><rect x="4" y="2" width="16" height="30" rx="3"/><path d="M10 27h4M24 12a6 6 0 0 1 0 10M27 9a10 10 0 0 1 0 16"/></svg>
<div class="abs f-h" style="left:907px;top:3901px;font-size:16px">Contact Us</div>
<div class="abs f-p" style="left:907px;top:3925px">(44) 555-0102-78</div>
<svg class="abs" style="left:862px;top:3972px" width="34" height="34" viewBox="0 0 34 34" fill="none" stroke="var(--orange)" stroke-width="2"><rect x="3" y="10" width="28" height="20"/><path d="M3 10l14 11 14-11M9 10V4h16v6"/></svg>
<div class="abs f-h" style="left:907px;top:3973px;font-size:16px">Contact Us</div>
<div class="abs f-p" style="left:907px;top:3997px">(44) 555-0102-78</div>

<div class="abs center f-p" style="top:4142px;font-size:14px;font-weight:600">Lumen Systems</div>
<div class="abs" style="left:1064px;top:4138px;width:32px;height:32px;background:var(--orange);display:flex;align-items:center;justify-content:center">
  <svg width="14" height="9" viewBox="0 0 14 9" fill="none" stroke="#fff" stroke-width="2"><path d="M1 8l6-6 6 6"/></svg></div>

</body>
</html>
```